International Energy Consultancy requires a "Company Capabilities Statement" in the for...

We need a capability statement polished, using the design and words provided. I have included a mockup/draft for reference. I have also added in our Company LogoWhat I would like at the end this, is to be able to tailor it depending on which client etc we are sending it to, for example change the text, case study and photograph etc).By way of background, Corvanta Partners is an expert team consultants with skills across the energy sector. https://corvantapartners.example/

Colors

Designer to choose colors to be used in the design.

Requirements
Must have
• View ppt provided to see what content is requires

```html
<!DOCTYPE html>
<html lang="en">
<head>
<meta charset="utf-8">
<title>Corvanta Partners – Capabilities Statement</title>
<link rel="stylesheet" href="https://fonts.googleapis.com/css2?family=Ubuntu:wght@300;400;500&display=swap">
<style>
  :root {
    --paper: #ffffff;
    --ink: #3a3a3a;
    --ink-dark: #1e1e1e;
    --sea: #cfe4ee;
    --sea-deep: #bcd8e6;
    --photo-blue: #1d3c8c;
    --photo-red: #b42a2a;
    --photo-green: #16924a;
    --brand-green: #2f9a45;
    --pattern: #ececec;
  }
  * { box-sizing: border-box; margin: 0; padding: 0; }
  html, body { width: 1200px; height: 857px; overflow: hidden; background: var(--paper); }
  body { font-family: "Ubuntu", sans-serif; color: var(--ink); position: relative; }

  .top-panel { position: absolute; left: 0; top: 0; width: 1200px; height: 379px; background: var(--paper); }
  .top-texture {
    position: absolute; right: 0; top: 0; width: 560px; height: 379px;
    background: linear-gradient(110deg, rgba(255,255,255,1) 0%, var(--pattern) 45%, #f2f2f2 100%);
  }

  .section { position: absolute; }
  .section h2 { font-weight: 300; font-size: 19px; color: var(--ink-dark); letter-spacing: -0.3px; margin-bottom: 6px; }
  .section p, .section li { font-size: 12px; line-height: 13px; font-weight: 400; }
  .section li { list-style: none; padding-left: 8px; text-indent: -8px; margin-bottom: 2.7px; }
  .section li::before { content: "• "; }
  .section p { margin-bottom: 3px; }

  .services { left: 52px; top: 76px; width: 330px; }
  .case-study { left: 430px; top: 76px; width: 355px; }

  .brand { position: absolute; left: 906px; top: 182px; display: flex; align-items: center; gap: 10px; }
  .brand-mark { width: 26px; height: 26px; background: var(--brand-green); }
  .brand-name { font-weight: 500; font-size: 24px; color: var(--ink-dark); }

  .map {
    position: absolute; left: 0; top: 379px; width: 803px; height: 478px;
    background: linear-gradient(135deg, #f1d9cc 0%, var(--sea) 28%, var(--sea-deep) 60%, #efdcc0 100%);
  }
  .experience { left: 52px; top: 442px; width: 500px; }
  .places { left: 52px; top: 619px; width: 730px; }

  .contact { position: absolute; left: 52px; top: 814px; font-size: 11px; font-weight: 500; color: var(--ink-dark); text-align: center; line-height: 14px; }

  .photo { position: absolute; }
  .photo-coast { left: 803px; top: 379px; width: 397px; height: 246px; background: linear-gradient(180deg, #2a4aa0 0%, var(--photo-blue) 55%, #2d5ab0 100%); }
  .photo-rig { left: 803px; top: 625px; width: 199px; height: 232px; background: linear-gradient(180deg, #c23434 0%, var(--photo-red) 60%, #7a1e1e 100%); }
  .photo-turbine { left: 1002px; top: 625px; width: 198px; height: 232px; background: linear-gradient(180deg, #1aa055 0%, var(--photo-green) 100%); }
</style>
</head>
<body>
  <div class="top-panel">
    <div class="top-texture" role="img" aria-label="Faint repeating hexagon pattern"></div>
  </div>

  <section class="section services">
    <h2>Services we provide</h2>
    <ul>
      <li>Solar PV, solar thermal, wind, battery energy storage project expertise</li>
      <li>Contract development &amp; negotiation</li>
      <li>Sophisticated financial modelling</li>
      <li>Strategic planning</li>
      <li>Feasibility studies, project concept design &amp; specification / Owner’s Engineer and construction supervision</li>
      <li>Stakeholder engagement</li>
      <li>Management Plans</li>
      <li>Project management, risk management</li>
      <li>Best Practice Environmental Options / Environmental Monitoring / Auditing</li>
      <li>Compliance for Environmental Legislation &amp; Regulations</li>
      <li>RE Training and capacity building</li>
      <li>Health and Safety training and auditing</li>
    </ul>
  </section>

  <section class="section case-study">
    <h2>Case study</h2>
    <p>Corvanta Partners recently conducted project management, feasibility studies, environmental and social impact assessment, oversight engineering and representation services as part of the UAE USD 50 million Pacific Partnership Fund.</p>
    <p>We optimised project development, design &amp; delivery for:</p>
    <ul>
      <li>Fiji Islands - 225 kW, 153 kW &amp; 153 kW PV, diesel hybrid systems</li>
      <li>Funafuti, Tuvalu - 500 kW PV, diesel/PV control</li>
      <li>Tarawa, Kiribati – 500 kW PV, diesel/PV control</li>
      <li>Nauru – 500 kW PV</li>
      <li>Majuro, Marshall Islands – 600 kW PV</li>
      <li>Pohnpei, Micronesia – 600 kW PV</li>
      <li>Palau islands – 100 kW &amp; 100 kW PV/diesel hybrid systems &amp; water purification</li>
      <li>Aleipata, Samoa – 550 kW wind</li>
    </ul>
  </section>

  <div class="brand">
    <span class="brand-mark"></span>
    <span class="brand-name">Corvanta Partners</span>
  </div>

  <div class="map" role="img" aria-label="Map of Asia-Pacific with project location markers"></div>

  <section class="section experience">
    <h2>Consultants experience</h2>
    <ul>
      <li>Commercial Lead for Solara One solar thermal plant / Wind farm on Sir Bani Yas Island / Northsea Array offshore opportunity</li>
      <li>Environmental and Social Safeguards for RE projects</li>
      <li>Wind Farm tender evaluations, ACT Wind Auctions I, II and III, Australia</li>
      <li>Consultancy advice for Ridgeway wind farm stages I, II and III, NZ</li>
      <li>Consultancy advice for Harrow I wind farm, Australia</li>
      <li>Technical due diligence of wind turbines</li>
    </ul>
  </section>

  <section class="section places">
    <h2>Places we’ve worked</h2>
    <ul>
      <li>Energy planning, grid integration studies, project design, ESIA, procurement and construction supervision in the Pacific. Includes projects such as 1.1 MWp PV with SCADA integrated remote control in Nauru, and 65 kWp PV, 72 kW/165 kWh BESS automated PV/battery/diesel hybrid system on Kayangel Island, Palau (in progress)</li>
      <li>RMI Electricity Roadmap</li>
      <li>Capacity building for Ministry of Electricity and Energy, Myanmar</li>
      <li>Project inception, feasibility studies, bidding documentation for solar and battery projects in the Caribbean</li>
      <li>Pacific Capacity Building and Training Workshops</li>
      <li>Energy sector opportunities and vision, Taranaki, New Zealand</li>
      <li>Solar Fuel-saver projects and Solar PV and grid integration projects</li>
      <li>GHG emissions and offsetting for a greenfields gas project in New Zealand</li>
    </ul>
  </section>

  <div class="contact">
    www.corvantapartners.example • contact@corvantapartners.example<br>
    +64 21 555 0147
  </div>

  <div class="photo photo-coast" role="img" aria-label="Blue-toned photograph of a coastline with a headland and waves"></div>
  <div class="photo photo-rig" role="img" aria-label="Red-toned photograph of an offshore oil and gas platform"></div>
  <div class="photo photo-turbine" role="img" aria-label="Green-toned photograph of a wind turbine"></div>
</body>
</html>
```